Meditation for IVF and infertility

I need a flyer inviting IVF patients to join my Meditation class, I would like to offer free meditation to ivf women and for couples this class is free every Thursday night at 5 pm
2465 west halloran blvd suite K Santa Barbara Ca 93274
larkvale-meditation.com for more details

```html
<!DOCTYPE html>
<html lang="en">
<head>
<meta charset="utf-8">
<title>Larkvale Meditation – Free Meditation Class</title>
<link href="https://fonts.googleapis.com/css2?family=Arimo:wght@700&family=Montserrat:wght@300;400;500&family=Oswald:wght@500;600&display=swap" rel="stylesheet">
<style>
  :root {
    --stage: #d6d6d6;
    --violet-deep: #513682;
    --violet-mid: #7c66b1;
    --pill-a: #9a3a85;
    --pill-b: #b04c95;
    --white: #ffffff;
    --photo-skin: #dcbcaa;
    --photo-cloth: #e9e6e4;
  }
  * { margin: 0; padding: 0; box-sizing: border-box; }
  html, body { width: 1200px; height: 1200px; overflow: hidden; }
  body {
    background: var(--stage);
    position: relative;
    font-family: "Montserrat", sans-serif;
  }
  .flyer {
    position: absolute;
    left: 191px; top: 62px;
    width: 789px; height: 1012px;
    background: linear-gradient(180deg, var(--violet-deep) 0%, var(--violet-mid) 46%, var(--violet-deep) 100%);
    overflow: hidden;
    color: var(--white);
  }
  .brand {
    position: absolute;
    left: 318px; top: 38px;
    width: 146px; height: 146px;
    border: 2px solid var(--white);
    border-radius: 50%;
    display: flex; flex-direction: column;
    align-items: center; justify-content: center;
    font-weight: 500;
    line-height: 1.15;
    text-align: center;
  }
  .brand-name { font-size: 22px; }
  .brand-sub { font-size: 11px; letter-spacing: 1px; }
  .blobs { position: absolute; left: 0; top: 0; }
  .photo {
    position: absolute;
    left: 152px; top: 202px;
    width: 486px; height: 470px;
    border-radius: 50%;
    background: radial-gradient(ellipse at 50% 52%, var(--photo-skin) 0%, var(--photo-cloth) 38%, rgba(200,196,205,0.6) 60%, rgba(200,196,205,0) 71%);
  }
  .free {
    position: absolute;
    z-index: 2;
    left: 144px; top: 604px;
    font-family: "Oswald", sans-serif;
    font-weight: 600;
    font-size: 60px;
    line-height: 1;
  }
  .headline {
    position: absolute;
    left: 0; width: 100%; top: 741px;
    text-align: center;
    font-family: "Arimo", sans-serif;
    font-weight: 700;
    font-size: 49px;
    line-height: 1;
    white-space: nowrap;
  }
  .subline {
    position: absolute;
    left: 0; width: 100%; top: 803px;
    text-align: center;
    font-weight: 400;
    font-size: 25px;
    line-height: 1;
    letter-spacing: 0.5px;
  }
  .schedule {
    position: absolute;
    left: 180px; top: 852px;
    width: 440px; height: 51px;
    border-radius: 26px;
    background: linear-gradient(180deg, var(--pill-b), var(--pill-a));
    display: flex; align-items: center; justify-content: center;
    font-family: "Oswald", sans-serif;
    font-weight: 500;
    font-size: 35px;
    line-height: 1;
  }
  .contact {
    position: absolute;
    left: 0; width: 100%;
    display: flex; align-items: center; justify-content: center;
    gap: 7px;
    font-weight: 300;
    line-height: 1;
  }
  .address { top: 925px; font-size: 17px; }
  .website { top: 961px; font-size: 14px; letter-spacing: 4px; }
  .contact svg { flex: none; }
</style>
</head>
<body>
  <main class="flyer">
    <div class="brand">
      <span class="brand-name">Larkvale</span>
      <span class="brand-sub">Meditation</span>
    </div>

    <svg class="blobs" width="789" height="1012" viewBox="0 0 789 1012" aria-hidden="true">
      <defs>
        <linearGradient id="blob-large" x1="0" y1="0" x2="1" y2="1">
          <stop offset="0" stop-color="#b0438a"/>
          <stop offset="0.6" stop-color="#7a3791"/>
          <stop offset="1" stop-color="#5f3a92"/>
        </linearGradient>
        <linearGradient id="blob-small" x1="0" y1="0" x2="1" y2="1">
          <stop offset="0" stop-color="#a7418a"/>
          <stop offset="1" stop-color="#6e4199" stop-opacity="0.4"/>
        </linearGradient>
      </defs>
      <circle cx="212" cy="630" r="96" fill="url(#blob-small)"/>
      <circle cx="408" cy="469" r="209" fill="url(#blob-large)"/>
    </svg>

    <div class="photo" role="img" aria-label="Photo of a pregnant woman meditating cross-legged in a white top and grey pants"></div>

    <div class="free">Free</div>

    <h1 class="headline">JOIN MY MEDITATION CLASS</h1>
    <p class="subline">Free meditation to ivf women and for couples</p>

    <div class="schedule">Every Thursday Night at 5 pm</div>

    <p class="contact address">
      <svg width="16" height="16" viewBox="0 0 24 24" aria-hidden="true">
        <circle cx="12" cy="12" r="12" fill="#fff"/>
        <path d="M12 5a5 5 0 0 0-5 5c0 3.6 5 9 5 9s5-5.4 5-9a5 5 0 0 0-5-5zm0 7a2 2 0 1 1 0-4 2 2 0 0 1 0 4z" fill="#5a3d8a"/>
      </svg>
      2465 west halloran blvd suite K Santa Barbara Ca 93274
    </p>
    <p class="contact website">
      <svg width="17" height="17" viewBox="0 0 24 24" fill="none" stroke="#fff" stroke-width="1.6" aria-hidden="true">
        <circle cx="12" cy="12" r="10"/>
        <ellipse cx="12" cy="12" rx="4.5" ry="10"/>
        <line x1="2" y1="12" x2="22" y2="12"/>
        <line x1="4" y1="7" x2="20" y2="7"/>
        <line x1="4" y1="17" x2="20" y2="17"/>
      </svg>
      larkvale-meditation.com
    </p>
  </main>
</body>
</html>
```